Letterhead Design Project

I need a letterhead design that is simple, modern, and colorful.

We publish novels that speak to female empowerment. With our fiction, we hope to encourage women to live boldly and love themselves without apology.

Our logo is red and teal so I'd like to see those colors continued in the letterhead.

The final design should be bold and inspiring.
Updates

Hello talented designers!

We will also be needing a business card design which will hopefully go to the designer of our letterhead. Please keep that in mind.

Thanks for all your efforts (in advance)!

I'd like the following information included:

Address - 4187 North Maplecrest Road, Suite #208, Linden Falls, Illinois 60492
Website - www.tallowquillpress.example
Email - info@tallowquillpress.example

Please see the updated files. The part of the logo that was red is now pink. And I've uploaded .eps and .ai formats. Thanks.

Target Market(s)

women, age 25+, college educated professionals

Requirements
Nice to have
• swirls or flourishes
Should not have
• dots or stripes

```html
<!DOCTYPE html>
<html lang="en">
<head>
<meta charset="utf-8">
<title>Tallowquill Press Stationery</title>
<link rel="stylesheet" href="https://fonts.googleapis.com/css2?family=Crimson+Pro:ital,wght@0,500;1,400&family=Questrial&family=Arimo:wght@700&display=swap">
<style>
  :root {
    --pink: #e0288a;
    --berry: #a8215f;
    --teal: #45b9dc;
    --teal-deep: #1f6f8f;
    --navy: #1f4a6e;
    --grey-text: #6b6b6b;
    --paper: #ffffff;
    --backdrop: #efefef;
  }
  * { box-sizing: border-box; margin: 0; padding: 0; }
  html, body { width: 1200px; height: 1000px; overflow: hidden; }
  body {
    background: radial-gradient(ellipse at 55% 45%, #fbfbfb 0%, var(--backdrop) 75%);
    position: relative;
    font-family: "Questrial", sans-serif;
  }
  .sheet {
    position: absolute;
    background: var(--paper);
    box-shadow: 0 6px 18px rgba(0,0,0,0.18);
    overflow: hidden;
  }
  .wordmark {
    font-family: "Crimson Pro", serif;
    font-weight: 500;
    line-height: 1;
    white-space: nowrap;
  }
  .tagline {
    font-family: "Crimson Pro", serif;
    font-style: italic;
    font-weight: 400;
    line-height: 1.2;
    white-space: nowrap;
  }
  .accent { position: absolute; left: 0; bottom: 0; width: 100%; display: block; }

  /* Letterhead */
  .letterhead { left: 470px; top: 50px; width: 660px; height: 854px; }
  .letterhead .brand { position: absolute; left: 38px; top: 40px; }
  .letterhead .wordmark { color: var(--pink); font-size: 26px; }
  .letterhead .tagline { color: var(--navy); font-size: 12px; margin-top: 4px; }
  .letterhead .contact {
    position: absolute; right: 40px; bottom: 176px;
    text-align: right; font-size: 13px; color: var(--grey-text); line-height: 1.35;
    font-style: normal;
  }
  .letterhead .contact .email { color: var(--pink); margin-top: 10px; }
  .letterhead .contact .web { color: var(--teal-deep); font-family: "Arimo", sans-serif; font-weight: 700; font-size: 12.5px; }

  /* Business card front */
  .card-front {
    left: 100px; top: 232px; width: 350px; height: 200px;
    background: linear-gradient(180deg, var(--pink) 0%, var(--pink) 55%, #a31e62 100%);
  }
  .card-front .brand { position: absolute; left: 0; right: 0; top: 80px; text-align: center; }
  .card-front .wordmark { color: #ffffff; font-size: 26px; }
  .card-front .tagline { color: #ffffff; font-size: 12px; margin-top: 5px; }

  /* Business card back */
  .card-back { left: 165px; top: 440px; width: 350px; height: 200px; }
  .card-back .details {
    position: absolute; right: 22px; top: 20px; text-align: right; color: var(--grey-text);
    font-style: normal;
  }
  .card-back .name { font-size: 16px; }
  .card-back .role { font-size: 11px; color: var(--pink); margin-top: 1px; }
  .card-back .address { font-size: 10.5px; line-height: 1.35; margin-top: 22px; }
  .card-back .email { font-size: 11px; color: var(--pink); margin-top: 7px; }
</style>
</head>
<body>

<section class="sheet card-front" aria-label="Business card front">
  <div class="brand">
    <div class="wordmark">Tallowquill Press</div>
    <div class="tagline">Bold stories for women who write their own endings.</div>
  </div>
</section>

<section class="sheet letterhead" aria-label="Letterhead">
  <header class="brand">
    <div class="wordmark">Tallowquill Press</div>
    <div class="tagline">Bold stories for women who write their own endings.</div>
  </header>
  <address class="contact">
    <div>4187 North Maplecrest Road,</div>
    <div>Suite #208, Linden Falls, Illinois 60492</div>
    <div class="email">info@tallowquillpress.example</div>
    <div class="web">www.tallowquillpress.example</div>
  </address>
  <svg class="accent" viewBox="0 0 660 140" height="140" preserveAspectRatio="none" aria-hidden="true">
    <defs>
      <linearGradient id="lh-base" x1="0" y1="0" x2="1" y2="0">
        <stop offset="0" stop-color="var(--teal-deep)"/>
        <stop offset="1" stop-color="var(--teal)"/>
      </linearGradient>
    </defs>
    <path d="M0,118 Q330,60 660,20 L660,140 L0,140 Z" fill="url(#lh-base)"/>
    <path d="M0,100 Q330,44 660,4 L660,10 Q330,52 0,108 Z" fill="var(--pink)"/>
  </svg>
</section>

<section class="sheet card-back" aria-label="Business card back">
  <address class="details">
    <div class="name">Evelyn Hartwell</div>
    <div class="role">Director</div>
    <div class="address">4187 North Maplecrest Road, Suite #208<br>Linden Falls, Illinois 60492</div>
    <div class="email">info@tallowquillpress.example</div>
  </address>
  <svg class="accent" viewBox="0 0 350 44" height="44" preserveAspectRatio="none" aria-hidden="true">
    <defs>
      <linearGradient id="bc-base" x1="0" y1="0" x2="1" y2="0">
        <stop offset="0" stop-color="var(--teal-deep)"/>
        <stop offset="1" stop-color="var(--teal)"/>
      </linearGradient>
    </defs>
    <path d="M0,38 Q175,24 350,10 L350,44 L0,44 Z" fill="url(#bc-base)"/>
    <path d="M0,31 Q175,17 350,3 L350,6 Q175,20 0,34 Z" fill="var(--pink)"/>
  </svg>
</section>

</body>
</html>
```